Simple, elegant, business card design required

Hi designers,I am looking for a simple yet elegant business card design.

Please make use of my logo (attached); you are free to tweak the logo should you wish to do so.

Our business is involved in many different fields - almost all of them involved in some form of "design", so that's really one of the key things I want to portray. I do not wish to specify which field of design, exactly.

I prefer white on black (or just monochromatic), but if you have a different, creative idea, I am open to that too.

You can use artsy photographs provided that you have the license to use those. Please feel free to ask me any questions.
Updates

Project Deadline Extended Reason: Small extension for potential revisions. Did not get the time to provide as much feedback as I can. Added Wednesday, July 09, 2014

Target Market(s)

High-end customers looking for design consultancy

Industry/Entity Type

Business

Contact Information for Business Card

Name: Gareth Moonfield
Position: Creative Director
Mobile: +155603928174
Address: Barrow Lane, Ashcombe upon Wyre, Hollingshire GL12 4RT
Website: torvakest.com (not launched yet)

Requirements
Must have
• Design layout must be clean, original, and text must be readable when printed.
Should not have
• ~ No business card templates please. Anyone using this will be reported.
• ~ Please don't spam entries.

```html
<!DOCTYPE html>
<html lang="en">
<head>
<meta charset="utf-8">
<title>Torvakest — Business Card</title>
<link rel="stylesheet" href="https://fonts.googleapis.com/css2?family=Oswald:wght@300&family=Roboto+Condensed:wght@700&family=Crimson+Text&display=swap">
<style>
  :root {
    --page: #ffffff;
    --card: #231f20;
    --ink: #ffffff;
    --icon-disc: #58585a;
  }
  * { margin: 0; padding: 0; box-sizing: border-box; }
  html, body { width: 1200px; height: 1000px; overflow: hidden; background: var(--page); }
  .canvas { position: relative; width: 1200px; height: 1000px; }
  .card {
    position: absolute; left: 145px; top: 220px;
    width: 910px; height: 560px;
    background: var(--card); color: var(--ink);
  }
  .brand-mark {
    position: absolute; left: 128px; top: 148px;
    width: 264px; height: 264px;
  }
  .wordmark {
    position: absolute; left: 482px; top: 80px;
    font-family: "Oswald", sans-serif; font-weight: 300;
    font-size: 62px; letter-spacing: 0.3em; line-height: 1;
    white-space: nowrap;
  }
  .identity {
    position: absolute; left: 500px; top: 222px; width: 400px;
    text-align: center; font-family: "Roboto Condensed", sans-serif; font-weight: 700;
  }
  .identity .name { font-size: 44px; line-height: 1.1; text-shadow: 2px 2px 3px rgba(0,0,0,.6); }
  .identity .role { font-size: 28px; line-height: 1.3; margin-top: 4px; padding-right: 30px; }
  .contacts {
    position: absolute; left: 505px; top: 374px; list-style: none;
    font-family: "Crimson Text", serif; font-size: 22px;
  }
  .contacts li { display: flex; align-items: flex-start; margin-bottom: 8px; line-height: 32px; white-space: nowrap; }
  .contacts .icon { flex: none; width: 32px; height: 32px; margin-right: 13px; }
  .contacts .spacer { width: 32px; margin-right: 13px; flex: none; }
</style>
</head>
<body>
<div class="canvas">
  <section class="card">
    <svg class="brand-mark" viewBox="0 0 264 264" aria-hidden="true">
      <circle cx="132" cy="132" r="116" fill="none" stroke="var(--ink)" stroke-width="28"/>
    </svg>

    <div class="wordmark">TORVAKEST</div>

    <div class="identity">
      <div class="name">Gareth Moonfield</div>
      <div class="role">Creative Director</div>
    </div>

    <ul class="contacts">
      <li>
        <svg class="icon" viewBox="0 0 32 32" aria-hidden="true">
          <circle cx="16" cy="16" r="16" fill="var(--icon-disc)"/>
          <rect x="11" y="7" width="10" height="18" rx="2" fill="var(--ink)"/>
          <rect x="12.5" y="10" width="7" height="11" fill="var(--icon-disc)"/>
        </svg>
        <span>+155603928174</span>
      </li>
      <li>
        <svg class="icon" viewBox="0 0 32 32" aria-hidden="true">
          <circle cx="16" cy="16" r="16" fill="var(--icon-disc)"/>
          <path d="M6 16 L16 7 L26 16 L23 16 L23 24 L18.5 24 L18.5 19 L13.5 19 L13.5 24 L9 24 L9 16 Z" fill="var(--ink)"/>
        </svg>
        <span>Barrow Lane, Ashcombe upon Wyre,</span>
      </li>
      <li>
        <span class="spacer"></span>
        <span>Hollingshire GL12 4RT</span>
      </li>
      <li>
        <svg class="icon" viewBox="0 0 32 32" aria-hidden="true">
          <circle cx="16" cy="16" r="16" fill="var(--icon-disc)"/>
          <rect x="9" y="9" width="14" height="10" fill="none" stroke="var(--ink)" stroke-width="1.6"/>
          <rect x="6" y="20.5" width="20" height="2.5" fill="var(--ink)"/>
        </svg>
        <span>torvakest.com</span>
      </li>
    </ul>
  </section>
</div>
</body>
</html>
```